Need A Standard Musical Download Website

We are looking for a talented designer to create a unique web design for our startup Music website called Vorlen Music.
The website should be responsive and filled with some creative stuffs along with bright colors.

Vorlen music is a website loaded with different types of music and capable of downloading the requested music by its users.
There will be categories of music which would be sorted by the genre. They include RnB, Hip-Hop, Afro pop, Pop, Dancehall and Reggae).

DESIGN STYLE/THEME

Creative, trendy, colorful, unique, and easy to use. You have freedom of selecting which ever color suits you. The design must be energetic and attractive.

NAVIGATION

HOME-MUSIC(RnB, Hip hop, Afro pop, POP, dancehall, Reggae)-ARTISTE-NEWS-LOGIN

PAGES REQUIRED
------------
1)Home Page
2)Music

FONTS
GOOGLE FONTS is strongly recommended.

Designers can get inspiration from https://tunebarrowk.com

Industry/Entity Type

Startup

```html
<!DOCTYPE html>
<html lang="en">
<head>
<meta charset="utf-8">
<title>Vorlen Music – Home</title>
<link href="https://fonts.googleapis.com/css2?family=Montserrat:wght@600;700;800&family=Open+Sans:wght@400;600;700&display=swap" rel="stylesheet">
<style>
:root{
  --night:#1b0a33;
  --plum:#3a0b5e;
  --magenta:#c0157e;
  --violet:#5b1aa0;
  --player:#120d2e;
  --teal:#1f8fae;
  --coral:#e2405a;
  --gold:#f7c23a;
  --blue:#2b8be0;
  --grey-bg:#eeeff2;
  --ink:#333;
  --muted:#888;
  --white:#fff;
}
*{box-sizing:border-box;margin:0;padding:0}
html,body{width:814px;height:1200px;overflow:hidden}
body{font-family:"Open Sans",Arial,sans-serif;color:var(--ink);background:var(--white);position:relative}
.site-header{position:absolute;top:0;left:0;width:814px;height:40px;background:rgba(20,6,38,.92);display:flex;align-items:center;padding:0 40px;z-index:3}
.brand{display:flex;align-items:center;gap:6px;font-family:"Montserrat",sans-serif;font-weight:700;font-size:16px;color:var(--white)}
.brand-dot{width:12px;height:12px;border-radius:50%;background:var(--coral)}
.main-nav{display:flex;gap:22px;margin-left:auto;margin-right:22px}
.main-nav a{color:var(--white);text-decoration:none;font-size:9px;font-weight:700;letter-spacing:.5px}
.header-search{width:96px;height:18px;border:1px solid rgba(255,255,255,.35);border-radius:2px;background:transparent;color:#ccc;font-size:8px;padding:0 6px;display:flex;align-items:center}
.login-btn{margin-left:10px;background:var(--blue);color:var(--white);font-size:8px;font-weight:700;padding:4px 12px;border-radius:2px}

.hero{position:absolute;top:0;left:0;width:814px;height:280px;background:linear-gradient(120deg,#2a0b54 0%,#5e1486 35%,#b3167f 60%,#3d0d6a 100%);overflow:hidden}
.hero svg.bands{position:absolute;left:0;top:0}
.trending-title{position:absolute;top:55px;left:40px;font-family:"Montserrat",sans-serif;font-weight:800;font-size:17px;color:var(--gold);letter-spacing:.5px}
.player{position:absolute;top:95px;left:100px;width:614px;height:78px;background:var(--player);border-radius:3px;display:flex;align-items:center;padding:0 10px;gap:14px}
.player-art{width:86px;height:60px;background:linear-gradient(135deg,#b89a7a,#6d4a3a)}
.player-body{flex:1}
.now-line{font-size:9px;font-weight:700;color:var(--white);display:flex;gap:18px}
.now-line em{font-style:normal;color:var(--coral)}
.player-controls{display:flex;align-items:center;gap:10px;margin-top:12px}
.ctrl{display:flex;align-items:center;gap:5px;font-size:6px;color:#bbb;font-weight:700;line-height:1.1}
.ctrl i{width:16px;height:16px;border-radius:50%;display:block}
.progress{flex:1;height:3px;background:#3a3560;position:relative;margin-left:18px}
.progress::before{content:"";position:absolute;left:0;top:0;width:40%;height:3px;background:var(--coral)}
.player-time{font-size:7px;color:#aaa}
.hero-search{position:absolute;top:232px;left:287px;width:240px;height:26px;display:flex}
.hero-search span{flex:1;background:var(--white);border-radius:2px 0 0 2px;font-size:8px;color:#999;padding:7px 8px}
.hero-search b{width:26px;background:var(--blue);border-radius:0 2px 2px 0;display:flex;align-items:center;justify-content:center}

.section-title{font-family:"Montserrat",sans-serif;font-weight:800;font-size:17px;letter-spacing:.3px}
.view-all{font-size:7px;font-weight:700;color:var(--teal);letter-spacing:.3px}
.top-songs{position:absolute;top:308px;left:40px;width:734px}
.top-songs .section-title{color:var(--teal)}
.songs-head{display:flex;justify-content:space-between;align-items:center;border-bottom:1px solid #ddd;padding-bottom:8px}
.song-row{display:flex;gap:3px;margin-top:12px}
.song-card{flex:1;border:1px solid #e3e3e3;background:var(--white)}
.song-photo{height:92px}
.song-meta{display:flex;justify-content:space-between;align-items:center;padding:5px 6px}
.song-meta strong{display:block;font-size:7px;color:#444}
.song-meta small{font-size:6px;color:var(--coral)}
.dl-icon{width:14px;height:14px;border-radius:2px;background:var(--coral)}
.dots{display:flex;gap:4px;justify-content:center;margin-top:14px}
.dots i{width:5px;height:5px;border-radius:50%;background:#ccc;display:block}
.dots i.on{background:var(--teal)}

.deco-notes{position:absolute;left:0;top:290px}

.top-artists{position:absolute;top:552px;left:40px;width:734px}
.top-artists .section-title{text-align:center;color:var(--coral)}
.artists-head{position:relative;height:24px}
.artists-head .view-all{position:absolute;right:0;top:26px}
.artist-box{margin-top:14px;border:1px solid #f0b7c2;height:112px;display:flex;padding:8px;gap:18px;background:var(--white)}
.artist-feature{width:104px;text-align:center}
.artist-feature .photo{height:80px;background:linear-gradient(135deg,#e7c894,#b77e54)}
.artist-feature span{display:block;font-size:7px;font-weight:700;margin-top:4px}
.artist-grid{flex:1;display:grid;grid-template-columns:repeat(3,1fr);gap:10px 14px;align-content:center;position:relative}
.artist-item{display:flex;gap:6px;align-items:center}
.artist-item .thumb{width:38px;height:38px}
.artist-item strong{display:block;font-size:7px}
.artist-item small{display:block;font-size:6px;color:var(--muted)}
.artist-item .acts{display:flex;gap:3px;margin-top:3px}
.artist-item .acts i{width:10px;height:10px;border-radius:50%;display:block;background:var(--coral)}
.artist-item .acts i+i{background:var(--teal)}
.more{position:absolute;right:0;bottom:-4px;font-size:7px;font-weight:700;color:var(--teal)}
.top-artists .dots{margin-top:16px}
.top-artists .dots i.on{background:var(--coral)}

.latest{position:absolute;top:732px;left:0;width:814px;height:280px;background:var(--grey-bg);padding:24px 40px;display:flex;gap:40px}
.latest .section-title{color:var(--teal);font-size:16px;margin-bottom:14px}
.tracks{width:330px}
.track-cols{display:flex;gap:20px}
.track-cols ul{list-style:none;flex:1}
.track-cols li{font-size:7px;color:#555;padding:4px 0;display:flex;gap:5px;align-items:center}
.track-cols li::before{content:"";width:7px;height:7px;border-radius:50%;background:var(--teal);flex:none}
.news{flex:1}
.news-grid{display:grid;grid-template-columns:1fr 1fr;gap:12px 18px}
.news-item{display:flex;gap:6px}
.news-item .thumb{width:34px;height:30px;flex:none}
.news-item p{font-size:7px;line-height:1.3;color:#444}
.news-item small{font-size:6px;color:var(--muted)}

.site-footer{position:absolute;top:1012px;left:0;width:814px;height:170px;background:linear-gradient(120deg,#24094a 0%,#4c1078 40%,#9b1479 75%,#2a0b54 100%);padding:30px 60px;display:flex}
.footer-brand .brand{font-size:18px}
.socials{display:flex;gap:4px;margin-top:10px}
.socials i{width:12px;height:12px;border-radius:50%;display:block;background:var(--blue)}
.socials i:nth-child(2){background:var(--coral)}
.socials i:nth-child(3){background:var(--teal)}
.socials i:nth-child(4){background:var(--gold)}
.footer-links{display:flex;gap:50px;margin-left:80px}
.footer-links ul{list-style:none}
.footer-links li{font-size:7px;color:#ddd;font-weight:600;padding:2px 0}
.newsletter{margin-left:auto;width:150px}
.newsletter h4{font-size:7px;color:var(--white);font-weight:700;letter-spacing:.5px}
.newsletter span{display:block;margin-top:6px;background:var(--white);height:18px;font-size:7px;color:#999;padding:4px 6px}
.newsletter b{display:inline-block;margin-top:6px;background:var(--blue);color:var(--white);font-size:7px;padding:4px 10px}
.copyright{position:absolute;top:1182px;left:0;width:814px;height:18px;background:var(--night);color:#999;font-size:6px;text-align:center;line-height:18px}
</style>
</head>
<body>

<section class="hero">
  <svg class="bands" width="814" height="280" viewBox="0 0 814 280" aria-hidden="true">
    <polygon points="0,190 814,150 814,200 0,240" fill="#e2405a" opacity=".35"/>
    <polygon points="0,230 814,190 814,230 0,280" fill="#2b8be0" opacity=".3"/>
    <polygon points="0,255 814,240 814,280 0,280" fill="#f7c23a" opacity=".25"/>
    <polygon points="300,0 520,0 380,280 200,280" fill="#ffffff" opacity=".04"/>
  </svg>
  <h2 class="trending-title">TRENDING NOW!</h2>
  <div class="player">
    <div class="player-art" role="img" aria-label="Album cover of the track now playing"></div>
    <div class="player-body">
      <p class="now-line"><span><em>PLAYING NOW:</em> ROCK &amp; ROLL 2011 – RELOADED</span><span><em>ARTIST:</em> DARA VANCE</span></p>
      <div class="player-controls">
        <span class="ctrl"><i style="background:var(--coral)"></i>ADD TO<br>FAVOURITE</span>
        <span class="ctrl"><i style="background:var(--teal)"></i>DOWNLOAD<br>NOW</span>
        <div class="progress"></div>
        <span class="player-time">01:24 / 03:45</span>
        <svg width="40" height="12" viewBox="0 0 40 12" aria-hidden="true"><path d="M2 1 L10 6 L2 11Z M14 1h3v10h-3z M20 1h3v10h-3z M28 4h3l4-3v10l-4-3h-3z" fill="#ccc"/></svg>
      </div>
    </div>
  </div>
  <div class="hero-search"><span>Enter any search</span><b><svg width="11" height="11" viewBox="0 0 11 11"><circle cx="4.5" cy="4.5" r="3.3" stroke="#fff" stroke-width="1.4" fill="none"/><path d="M7 7l3 3" stroke="#fff" stroke-width="1.4"/></svg></b></div>
</section>

<header class="site-header">
  <div class="brand"><span class="brand-dot"></span>Vorlen Music</div>
  <nav class="main-nav"><a href="#">HOME</a><a href="#">MUSIC</a><a href="#">ARTISTS</a><a href="#">NEWS</a></nav>
  <div class="header-search">Search</div>
  <span class="login-btn">LOGIN</span>
</header>

<section class="top-songs">
  <div class="songs-head"><h2 class="section-title">TOP 10 SONGS</h2><span class="view-all">VIEW ALL SONGS ›</span></div>
  <div class="song-row">
    <article class="song-card"><div class="song-photo" role="img" aria-label="Singer performance photo" style="background:linear-gradient(135deg,#c9a68a,#6b4a3e)"></div><div class="song-meta"><div><strong>SHARE OF YOU</strong><small>Download</small></div><i class="dl-icon"></i></div></article>
    <article class="song-card"><div class="song-photo" role="img" aria-label="Artist portrait photo" style="background:linear-gradient(135deg,#8a3b4a,#2c1a24)"></div><div class="song-meta"><div><strong>SHARE OF YOU</strong><small>Download</small></div><i class="dl-icon"></i></div></article>
    <article class="song-card"><div class="song-photo" role="img" aria-label="Artist on stage photo" style="background:linear-gradient(135deg,#e2c2a8,#9a6f5a)"></div><div class="song-meta"><div><strong>SHARE OF YOU</strong><small>Download</small></div><i class="dl-icon"></i></div></article>
    <article class="song-card"><div class="song-photo" role="img" aria-label="Guitarist under concert light photo" style="background:linear-gradient(135deg,#f2b24a,#b5421f)"></div><div class="song-meta"><div><strong>SHARE OF YOU</strong><small>Download</small></div><i class="dl-icon"></i></div></article>
    <article class="song-card"><div class="song-photo" role="img" aria-label="Singer with microphone photo" style="background:linear-gradient(135deg,#b98a76,#5a3a36)"></div><div class="song-meta"><div><strong>SHARE OF YOU</strong><small>Download</small></div><i class="dl-icon"></i></div></article>
    <article class="song-card"><div class="song-photo" role="img" aria-label="Live concert crowd photo" style="background:linear-gradient(135deg,#7d3a8a,#2b1240)"></div><div class="song-meta"><div><strong>SHARE OF YOU</strong><small>Download</small></div><i class="dl-icon"></i></div></article>
  </div>
  <div class="dots"><i class="on"></i><i></i><i></i></div>
</section>

<section class="top-artists">
  <div class="artists-head"><h2 class="section-title">TOP 10 ARTISTS</h2><span class="view-all">VIEW ALL ARTISTS ›</span></div>
  <div class="artist-box">
    <div class="artist-feature"><div class="photo" role="img" aria-label="Featured artist portrait"></div><span>MARLA QUINN</span></div>
    <div class="artist-grid">
      <div class="artist-item"><div class="thumb" role="img" aria-label="Artist photo" style="background:#b07a6a"></div><div><strong>SHARE OF YOU</strong><small>12 Songs</small><div class="acts"><i></i><i></i></div></div></div>
      <div class="artist-item"><div class="thumb" role="img" aria-label="Artist photo" style="background:#7a4a5a"></div><div><strong>SHARE OF YOU</strong><small>12 Songs</small><div class="acts"><i></i><i></i></div></div></div>
      <div class="artist-item"><div class="thumb" role="img" aria-label="Artist photo" style="background:#c99a7a"></div><div><strong>SHARE OF YOU</strong><small>12 Songs</small><div class="acts"><i></i><i></i></div></div></div>
      <div class="artist-item"><div class="thumb" role="img" aria-label="Artist photo" style="background:#8e5a4a"></div><div><strong>SHARE OF YOU</strong><small>12 Songs</small><div class="acts"><i></i><i></i></div></div></div>
      <div class="artist-item"><div class="thumb" role="img" aria-label="Artist photo" style="background:#5a3a4a"></div><div><strong>SHARE OF YOU</strong><small>12 Songs</small><div class="acts"><i></i><i></i></div></div></div>
      <div class="artist-item"><div class="thumb" role="img" aria-label="Artist photo" style="background:#d0a88a"></div><div><strong>SHARE OF YOU</strong><small>12 Songs</small><div class="acts"><i></i><i></i></div></div></div>
      <span class="more">MORE »</span>
    </div>
  </div>
  <div class="dots"><i class="on"></i><i></i><i></i><i></i><i></i><i></i><i></i><i></i><i></i><i></i></div>
</section>

<section class="latest">
  <div class="tracks">
    <h2 class="section-title">LATEST MP3 TRACKS</h2>
    <div class="track-cols">
      <ul><li>Midnight Songs 2018</li><li>Wake Up Tonight Remix</li><li>Blue Lights Single</li><li>Golden Hour Mama</li><li>Where The River Runs</li></ul>
      <ul><li>Slow Drag Ft. Lil Sun</li><li>Big Sky Call Out</li><li>Velvet Dance Party</li><li>Hollow Spaces Remix</li><li>Night Drive Mix</li></ul>
    </div>
  </div>
  <div class="news">
    <h2 class="section-title">LATEST NEWS</h2>
    <div class="news-grid">
      <div class="news-item"><div class="thumb" role="img" aria-label="News photo" style="background:#a86a6a"></div><div><p>Lorem ipsum dolor sit amet elit</p><small>Jan 12, 2018</small></div></div>
      <div class="news-item"><div class="thumb" role="img" aria-label="News photo" style="background:#6a5a8a"></div><div><p>Lorem ipsum dolor sit amet elit</p><small>Jan 12, 2018</small></div></div>
      <div class="news-item"><div class="thumb" role="img" aria-label="News photo" style="background:#c4946a"></div><div><p>Lorem ipsum dolor sit amet elit</p><small>Jan 12, 2018</small></div></div>
      <div class="news-item"><div class="thumb" role="img" aria-label="News photo" style="background:#4a6a8a"></div><div><p>Lorem ipsum dolor sit amet elit</p><small>Jan 12, 2018</small></div></div>
      <div class="news-item"><div class="thumb" role="img" aria-label="News photo" style="background:#8a4a6a"></div><div><p>Lorem ipsum dolor sit amet elit</p><small>Jan 12, 2018</small></div></div>
      <div class="news-item"><div class="thumb" role="img" aria-label="News photo" style="background:#9a7a5a"></div><div><p>Lorem ipsum dolor sit amet elit</p><small>Jan 12, 2018</small></div></div>
    </div>
  </div>
</section>

<footer class="site-footer">
  <div class="footer-brand">
    <div class="brand"><span class="brand-dot"></span>Vorlen Music</div>
    <div class="socials"><i></i><i></i><i></i><i></i><i></i></div>
  </div>
  <div class="footer-links">
    <ul><li>HOME</li><li>MUSIC</li><li>ARTISTS</li><li>NEWS</li></ul>
    <ul><li>LOGIN</li><li>MY ACCOUNT</li><li>PRIVACY</li><li>CONTACT</li></ul>
  </div>
  <div class="newsletter">
    <h4>NEWSLETTER SIGNUP</h4>
    <span>Email Address</span>
    <b>SUBMIT</b>
  </div>
</footer>
<div class="copyright">© 2018 Vorlen Music | All Rights Reserved</div>

</body>
</html>
```